ZRD Roofing Billboard Design

Looking for a fresh new billboard design with my new headshot photo and using some info from my previous billboard and maybe website for design/content inspiration. My website is https://zrdroofing.com/

Also attached are my logo and current lawn sign design. I am looking for something simple, clean and modern. The landing page website should be 3816tops.com like my previous billboard has.

```html
<!DOCTYPE html>
<html lang="en">
<head>
<meta charset="utf-8">
<title>ZRD Roofing Billboard</title>
<link href="https://fonts.googleapis.com/css2?family=Anton&family=Roboto+Condensed:wght@700&family=Lora:wght@500&display=swap" rel="stylesheet">
<style>
  :root {
    --page-bg: #e9edf1;
    --board-white: #ffffff;
    --brand-green: #8fae1b;
    --brand-navy: #213a63;
    --photo-light: #d9dde2;
    --photo-mid: #9aa3ad;
    --photo-dark: #5b6672;
    --tagline: #2a3d5e;
  }
  html, body {
    margin: 0;
    width: 1200px;
    height: 1200px;
    overflow: hidden;
    background: var(--page-bg);
  }
  .billboard {
    position: absolute;
    left: 20px;
    top: 370px;
    width: 1160px;
    height: 460px;
    background: var(--board-white);
    overflow: hidden;
    box-shadow: 0 6px 24px rgba(0,0,0,.18);
  }
  .billboard-shapes {
    position: absolute;
    inset: 0;
  }
  .brand {
    position: absolute;
    left: 40px;
    top: 44px;
    width: 300px;
    display: flex;
    flex-direction: column;
    align-items: center;
    gap: 10px;
  }
  .brand-name {
    font-family: "Roboto Condensed", sans-serif;
    font-weight: 700;
    font-size: 32px;
    line-height: 1;
    color: var(--brand-navy);
  }
  .brand-dot {
    width: 64px;
    height: 64px;
    border-radius: 50%;
    background: var(--brand-green);
  }
  .brand-tagline {
    font-family: "Lora", serif;
    font-weight: 500;
    font-size: 19px;
    line-height: 1.2;
    color: var(--tagline);
  }
  .headline {
    position: absolute;
    left: 360px;
    top: 40px;
  }
  .headline-main {
    font-family: "Anton", sans-serif;
    font-size: 88px;
    line-height: 1;
    color: var(--brand-green);
    letter-spacing: 1px;
  }
  .headline-sub {
    font-family: "Roboto Condensed", sans-serif;
    font-weight: 700;
    font-size: 54px;
    line-height: 1;
    color: var(--brand-navy);
    margin-top: 4px;
  }
  .offer {
    display: flex;
    align-items: baseline;
    gap: 16px;
    margin-top: 4px;
  }
  .offer-label {
    font-family: "Roboto Condensed", sans-serif;
    font-weight: 700;
    font-size: 38px;
    line-height: 1;
    color: var(--brand-navy);
  }
  .offer-price {
    font-family: "Anton", sans-serif;
    font-size: 66px;
    line-height: 1;
    color: var(--brand-green);
  }
  .phone {
    position: absolute;
    left: 26px;
    top: 288px;
    font-family: "Roboto Condensed", sans-serif;
    font-weight: 700;
    font-size: 52px;
    line-height: 1.2;
    color: var(--board-white);
  }
  .web {
    position: absolute;
    left: 460px;
    top: 382px;
    font-family: "Roboto Condensed", sans-serif;
    font-weight: 700;
    font-size: 54px;
    line-height: 1.2;
    color: var(--board-white);
  }
</style>
</head>
<body>
  <div class="billboard">
    <svg class="billboard-shapes" width="1160" height="460" viewBox="0 0 1160 460">
      <defs>
        <linearGradient id="photoTone" x1="0" y1="0" x2="0" y2="1">
          <stop offset="0" stop-color="var(--photo-light)"/>
          <stop offset="0.55" stop-color="var(--photo-mid)"/>
          <stop offset="1" stop-color="var(--photo-dark)"/>
        </linearGradient>
      </defs>
      <g role="img" aria-label="Photo of a smiling roofer in a light blue shirt in front of a metal roof with a worker on top">
        <polygon points="752,0 1160,0 1160,460 860,460" fill="url(#photoTone)"/>
      </g>
      <polygon class="divider-stripe" points="720,0 752,0 860,460 828,460" fill="var(--brand-green)"/>
      <polygon class="phone-band" points="0,280 448,280 466,360 0,360" fill="var(--brand-green)"/>
      <polygon class="web-band" points="420,372 807,372 828,460 440,460" fill="var(--brand-navy)"/>
    </svg>

    <div class="brand">
      <span class="brand-name">ZRD Roofing LLC</span>
      <span class="brand-dot"></span>
      <span class="brand-tagline">Built Strong, Built Local</span>
    </div>

    <div class="headline">
      <div class="headline-main">FULL ROOF</div>
      <div class="headline-sub">REPLACEMENTS</div>
      <div class="offer">
        <span class="offer-label">Starting at</span>
        <span class="offer-price">$7,499</span>
      </div>
    </div>

    <div class="phone">(555) 217-4630</div>
    <div class="web">3816TOPS.com</div>
  </div>
</body>
</html>
```